Visitenkarten-Design Neutrale Verzollungs Agentur für den Grenzverkehr des Zollwesens
Sehr schnelle Umsetzung nach unserer Vorstellung,und sehr netter und guter Umgang in der Kominikation. tolvix hat unsere erwartung zu 100 % übertroffen.
Zielgruppe
Wir sind eine Neutrale Verzollungs Agentur für den Grenzverkehr des Zollwesens
Bluefield & Meridian Group
Wir führen für Kunden die Zollabwicklungen ab.
Seefracht - Bahnfracht-Luftfracht-LKW Fracht
Cargo - Hersteller Firmen und Endknden International
Aufgabenstellung
Rückseite sollte mitgestaltet werden

```html
<!DOCTYPE html>
<html lang="de">
<head>
<meta charset="utf-8">
<title>Transiva – Visitenkarte</title>
<link href="https://fonts.googleapis.com/css2?family=Open+Sans:wght@400;600;700&display=swap" rel="stylesheet">
<style>
  :root{
    --stage:#262626;
    --card-white:#ffffff;
    --ink:#4a4a4a;
    --ink-dark:#3c3c3c;
    --brand-blue:#4a8fd0;
    --brand-blue-light:#8fb8e6;
    --brand-blue-deep:#3f7fc4;
    --stripe:#2a3f6e;
  }
  *{margin:0;padding:0;box-sizing:border-box}
  html,body{width:1200px;height:801px;overflow:hidden}
  body{
    background:var(--stage);
    font-family:"Open Sans",Arial,sans-serif;
    display:flex;align-items:center;justify-content:center;gap:48px;
  }
  .card{
    width:525px;height:300px;position:relative;overflow:hidden;
    box-shadow:0 10px 30px rgba(0,0,0,.45);
  }
  /* front */
  .card--front{background:var(--card-white);color:var(--ink)}
  .card__band{position:absolute;inset:0;width:100%;height:100%}
  .brand{
    position:absolute;top:46px;left:0;right:0;text-align:center;
    display:flex;align-items:center;justify-content:center;gap:12px;
  }
  .brand__dot{width:18px;height:18px;border-radius:50%;background:var(--brand-blue)}
  .brand__name{font-size:40px;font-weight:600;color:var(--ink-dark);letter-spacing:.5px}
  .tagline{position:absolute;top:112px;left:0;right:0;text-align:center;font-weight:700;font-size:14px;color:var(--ink)}
  .countries{position:absolute;top:132px;left:0;right:0;text-align:center;font-size:12px;color:var(--ink)}
  .countries .sep{color:var(--brand-blue);padding:0 4px}
  .person{position:absolute;top:162px;left:0;right:0;text-align:center;font-size:19px;font-weight:600;color:var(--brand-blue)}
  .address{position:absolute;top:206px;left:0;right:0;text-align:center;font-size:11px;color:var(--ink)}
  .contacts{
    position:absolute;top:224px;left:0;right:0;
    display:flex;justify-content:center;gap:10px;font-size:10.5px;color:var(--ink);
  }
  .contacts span{display:flex;align-items:center;gap:3px}
  .contacts svg{width:10px;height:10px}
  /* back */
  .card--back{
    background:linear-gradient(135deg,#4f93d2 0%,var(--brand-blue) 50%,var(--brand-blue-deep) 100%);
    display:flex;align-items:center;justify-content:center;gap:16px;
  }
  .card--back .brand__dot{width:26px;height:26px;background:var(--brand-blue-light)}
  .card--back .brand__name{font-size:60px;color:var(--ink-dark)}
</style>
</head>
<body>

<section class="card card--front" aria-label="Visitenkarte Vorderseite">
  <svg class="card__band" viewBox="0 0 525 300" preserveAspectRatio="none" aria-hidden="true">
    <defs>
      <linearGradient id="bandGrad" x1="0" y1="0" x2="1" y2="0">
        <stop offset="0" stop-color="#3f7fc4"/>
        <stop offset="1" stop-color="#9cc2ea"/>
      </linearGradient>
    </defs>
    <polygon points="0,300 525,258 525,266 0,300" fill="url(#bandGrad)"/>
    <polygon points="0,286 525,252 525,258 0,292" fill="url(#bandGrad)" opacity=".55"/>
    <g fill="var(--stripe)">
      <rect x="20" y="262" width="4" height="30"/>
      <rect x="29" y="260" width="4" height="32"/>
      <rect x="38" y="258" width="4" height="34"/>
      <rect x="47" y="256" width="4" height="36"/>
    </g>
  </svg>

  <div class="brand">
    <span class="brand__name">Transiva</span>
    <span class="brand__dot"></span>
  </div>
  <p class="tagline">Bluefield &amp; Meridian Group</p>
  <p class="countries">Switzerland<span class="sep">|</span>Germany<span class="sep">|</span>Denmark<span class="sep">|</span>France</p>
  <p class="person">Weber Jonas</p>
  <p class="address">Lindenweg 12 4058 Basel Switzerland</p>
  <div class="contacts">
    <span><svg viewBox="0 0 10 10"><path d="M2 1l2 2-1 1.5a5 5 0 0 0 2.5 2.5L7 6l2 2-1.5 1.5C4 9 1 6 .5 2.5z" fill="var(--brand-blue)"/></svg>+49 761000123</span>
    <span><svg viewBox="0 0 10 10"><path d="M2 1l2 2-1 1.5a5 5 0 0 0 2.5 2.5L7 6l2 2-1.5 1.5C4 9 1 6 .5 2.5z" fill="var(--brand-blue)"/></svg>+41 610000456</span>
    <span><svg viewBox="0 0 10 10"><rect x=".5" y="2" width="9" height="6" rx="1" fill="var(--brand-blue)"/><path d="M.5 2.5L5 5.5l4.5-3" stroke="#fff" stroke-width=".8" fill="none"/></svg>info@transiva-beispiel</span>
    <span><svg viewBox="0 0 10 10"><circle cx="5" cy="5" r="4.3" fill="var(--brand-blue)"/><path d="M1 5h8M5 .7v8.6M5 .7c-2 2.5-2 6 0 8.6M5 .7c2 2.5 2 6 0 8.6" stroke="#fff" stroke-width=".6" fill="none"/></svg>www.transiva-beispiel.com</span>
  </div>
</section>

<section class="card card--back" aria-label="Visitenkarte Rückseite">
  <span class="brand__name">Transiva</span>
  <span class="brand__dot"></span>
</section>

</body>
</html>
```